Business card design needed

We require a business card and logo design for our tipper truck business which services the building and agricultural industries, based in Albury-Wodonga, Australia. The business name is 'Bramble Transport' and our business moto is 'if it's tippable, it's doable'.
If a tipper truck is to be included in the logo, the truck must not have a nose ie. the truck must have a flat front.
The moto for the Albury-Wodonga region is 'where the mountains meet the murray' (snowy mountains meet murray river-this may or may not be included in the image design)

Industry/Entity Type

Building

Contact Information for Business Card

BRAMBLE TRANSPORT PTY LTD
Complete Tipper Hire
If it fits the tray, it's on its way!
Tom Wexley
0491 570 183
brambletransport@mailnest.com.au
PO Box 819
Thornvale NSW 2648
ABN: 27 318 905 442

```html
<!DOCTYPE html>
<html lang="en">
<head>
<meta charset="utf-8">
<title>Bramble Transport Business Card</title>
<link rel="stylesheet" href="https://fonts.googleapis.com/css2?family=Ubuntu:wght@400;700&family=Kalam:wght@400&display=swap">
<style>
  :root {
    --page-bg: #e6e7ea;
    --card-bg: #3b404b;
    --card-bg-deep: #2f333c;
    --card-text: #f2f3f5;
    --card-muted: #c9ccd2;
    --logo-block: #8d939e;
    --truck-tone: #d9dbdf;
  }
  * { margin: 0; padding: 0; box-sizing: border-box; }
  html, body {
    width: 1200px;
    height: 861px;
    overflow: hidden;
    background: var(--page-bg);
  }
  .stage {
    width: 1200px;
    height: 861px;
    display: flex;
    align-items: center;
    justify-content: center;
  }
  .business-card {
    position: relative;
    width: 840px;
    height: 480px;
    border-radius: 26px;
    background: linear-gradient(160deg, var(--card-bg) 0%, var(--card-bg-deep) 100%);
    box-shadow: 0 18px 40px rgba(0, 0, 0, 0.28);
    color: var(--card-text);
    font-family: "Ubuntu", sans-serif;
    overflow: hidden;
  }
  .logo {
    position: absolute;
    top: 40px;
    right: 50px;
    width: 400px;
    text-align: center;
  }
  .logo-artwork {
    width: 400px;
    height: 120px;
    border-radius: 10px;
    background: linear-gradient(180deg, var(--truck-tone) 0%, var(--logo-block) 100%);
    opacity: 0.9;
  }
  .logo-name {
    margin-top: 14px;
    display: flex;
    align-items: center;
    justify-content: center;
    gap: 10px;
    font-size: 22px;
    font-weight: 700;
    letter-spacing: 1px;
    color: var(--card-text);
  }
  .logo-mark {
    width: 14px;
    height: 14px;
    background: var(--card-text);
  }
  .logo-tagline {
    margin-top: 8px;
    font-size: 17px;
    letter-spacing: 5px;
    color: var(--card-muted);
  }
  .contact {
    position: absolute;
    right: 60px;
    top: 262px;
    text-align: right;
  }
  .contact-name {
    font-size: 46px;
    font-weight: 700;
    letter-spacing: 1px;
    margin-bottom: 12px;
  }
  .contact-line {
    font-size: 20px;
    line-height: 29px;
    color: var(--card-text);
  }
  .motto {
    position: absolute;
    left: 56px;
    bottom: 48px;
    width: 360px;
    font-family: "Kalam", cursive;
    font-size: 38px;
    line-height: 46px;
    color: var(--card-text);
  }
  .motto-line-2 { padding-left: 36px; }
</style>
</head>
<body>
  <main class="stage">
    <article class="business-card">
      <header class="logo">
        <div class="logo-artwork" role="img" aria-label="Illustration of a flat-fronted tipper truck"></div>
        <div class="logo-name"><span class="logo-mark"></span>BRAMBLE TRANSPORT PTY LTD</div>
        <div class="logo-tagline">Complete Tipper Hire</div>
      </header>

      <section class="contact">
        <h1 class="contact-name">Tom Wexley</h1>
        <p class="contact-line">PO Box 819 Thornvale NSW 2648</p>
        <p class="contact-line">0491 570 183</p>
        <p class="contact-line">brambletransport@mailnest.com.au</p>
        <p class="contact-line">ABN: 27 318 905 442</p>
      </section>

      <p class="motto">
        <span class="motto-line-1">If it fits the tray,</span><br>
        <span class="motto-line-2">it's on its way!</span>
      </p>
    </article>
  </main>
</body>
</html>
```